Wine Shop Banners

Banner graphic/images required
Require banner images to match the present online wine shop.

www.kelterhaus-traube.de

The wine-shop presently has a very clean, simple design, lots of white space, which is very much the trend at the moment.

Requirements
Images or graphic design for present banners visible on the homepage

The colour and feeling of the banners must fit in with the present clean, simple design.

Work required
3 large slide-card/banners (can be more) and 3 smaller fixed banners below. Please view website to see present position of banners.

LARGE BANNERS x 3

Something special with white background within the banner space
White background on each slide-card. Small individual graphic image in the middle of the slide card. This could be either a simple element of wine:
ingredients, fruit (grape), bottle, cork, old bottle label etc. just displaying one item on each slide-card. Preferably with high quality graphic features.

Note:
We are trying the steer away from the classic stereotype wineshop design. The image/s should have a higher, individual graphic touch, which gives the design something different. Sometimes such artistic work is displayed in steampunk or even in nostalgic design, which leaves the viewer slightly memorized with the content.
To clarify: we are not looking for a full steampunk design but possibly certain elements of this will give you an idea what we mean. That is to say, the design can go slightly in this direction without going over the top. Something small but very eye-catching.

SMALLER BANNERS x 3

One idea is:
Showing a symbol e.g. - discount sign "%" against a white background but again with a high graphic quality.

Target Market(s)

People interested in purchasing wine.
Ages approx. 25 to 65

Industry/Entity Type

Shop

Requirements
Must have
• Something special with white background
• Small individual graphic image in the middle of the slide card.
Nice to have
• The image/s should have a higher, individual graphic touch, which gives the design something different. Something that leaves the viewer slightly memorized with the content.
Should not have
• Not the typical classical design that is often seen on wine shops.

```html
<!DOCTYPE html>
<html lang="en">
<head>
<meta charset="utf-8">
<title>Pure Organic Wine – Banner</title>
<link rel="stylesheet" href="https://fonts.googleapis.com/css2?family=Tinos&family=Gelasio:wght@500&family=Arimo&display=swap">
<style>
  :root {
    --page-bg: #ffffff;
    --banner-center: #ffffff;
    --banner-edge: #ececec;
    --title-green: #2f6a1a;
    --tagline-red: #8a1414;
    --offer-gold: #b39e00;
    --visual-top: #d9e6cc;
    --visual-bottom: #ecd2d5;
  }
  html, body {
    margin: 0;
    padding: 0;
    width: 1200px;
    height: 900px;
    overflow: hidden;
    background: var(--page-bg);
  }
  .canvas {
    position: relative;
    width: 1200px;
    height: 900px;
  }
  .banner {
    position: absolute;
    left: 28px;
    top: 186px;
    width: 1142px;
    height: 440px;
    background: var(--banner-center);
    box-shadow: inset 0 0 34px 14px var(--banner-edge);
    overflow: hidden;
  }
  .grape-visual {
    position: absolute;
    left: 0;
    top: 0;
    width: 340px;
    height: 420px;
    background: linear-gradient(180deg, var(--visual-top) 0%, var(--visual-bottom) 100%);
  }
  .banner-copy {
    position: absolute;
    right: 76px;
    top: 0;
    text-align: right;
  }
  .title {
    position: absolute;
    right: -3px;
    top: 71px;
    margin: 0;
    white-space: nowrap;
    font-family: "Tinos", "Times New Roman", serif;
    font-weight: 400;
    font-size: 72px;
    line-height: 1;
    color: var(--title-green);
    transform: scaleX(0.86);
    transform-origin: right center;
  }
  .tagline {
    position: absolute;
    right: 0;
    top: 196px;
    margin: 0;
    white-space: nowrap;
    font-family: "Gelasio", Georgia, serif;
    font-weight: 500;
    font-size: 23px;
    line-height: 1;
    color: var(--tagline-red);
  }
  .offer {
    position: absolute;
    right: -1.5px;
    top: 272px;
    margin: 0;
    white-space: nowrap;
    font-family: "Arimo", Arial, sans-serif;
    font-size: 40px;
    letter-spacing: 1.5px;
    line-height: 46px;
    color: var(--offer-gold);
  }
</style>
</head>
<body>
  <main class="canvas">
    <section class="banner">
      <div class="grape-visual" role="img" aria-label="Bunches of red and green grapes with vine leaves, splashing wine drops and falling grape halves"></div>
      <div class="banner-copy">
        <h1 class="title">PURE ORGANIC WINE</h1>
        <p class="tagline">Lorem ipsum dolor sit amet, consectetur adipisicing eiat nulla</p>
        <p class="offer">surprise of wine Gifts for<br>Someone Special</p>
      </div>
    </section>
  </main>
</body>
</html>
```